Business Card Design

We custom build & and install Air filtration systems for mining machines - the system filters the air going into the cabin to protect the operator/driver Examples of the machines we install our units to would be Tarrowind or Velorin. Australian owned company Our company colors are sky blue with polished Stainless steel lettering & framing. I have a logo which I will upload but I would like the new image to be crisper.

Industry/Entity Type

Business

Contact Information for Business Card

Company name - Cleanwarden Pty Ltd
Tom Pellworth - Position - Sales & Product Development Contact numbers Mob 0498 352 619 Tel - 07 3941 2586
Address - 174 Marlow St, Fernhollow, Brisbane 4108, Australia

Colors
0255a3

Requirements
Must have
• sky blue & polished chrome lettering

```html
<!DOCTYPE html>
<html lang="en">
<head>
<meta charset="utf-8">
<title>Cleanwarden Business Card</title>
<link rel="stylesheet" href="https://fonts.googleapis.com/css2?family=Exo+2:wght@400;500;600;800&display=swap">
<style>
  :root {
    --backdrop: #d9d9d9;
    --card: #ffffff;
    --brand-blue: #243f91;
    --ink: #2b2b2b;
    --on-blue: #ffffff;
  }
  * { margin: 0; padding: 0; box-sizing: border-box; }
  html, body {
    width: 1200px; height: 949px; overflow: hidden;
    background: var(--backdrop);
    font-family: "Exo 2", sans-serif;
  }
  .card {
    position: absolute; left: 250px;
    width: 700px; height: 400px;
    background: var(--card);
    border-radius: 26px;
    overflow: hidden;
    box-shadow: 0 6px 18px rgba(0,0,0,0.18);
  }
  .card--front { top: 45px; }
  .card--back { top: 495px; }

  /* Front */
  .brand {
    position: absolute; inset: 0;
    display: flex; align-items: center; justify-content: center; gap: 20px;
  }
  .brand-mark { width: 44px; height: 44px; background: var(--brand-blue); }
  .brand-name {
    color: var(--brand-blue);
    font-weight: 800; font-size: 64px; letter-spacing: 1px;
  }

  /* Back */
  .info-band {
    position: absolute; left: 0; top: 180px;
    width: 100%; height: 190px;
    background: var(--brand-blue);
  }
  .icon-badge {
    position: absolute; width: 40px; height: 40px; border-radius: 50%;
    background: var(--brand-blue);
    display: flex; align-items: center; justify-content: center;
  }
  .icon-badge svg { width: 22px; height: 22px; fill: var(--on-blue); }
  .icon-badge--light { background: var(--on-blue); width: 54px; height: 54px; }
  .icon-badge--light svg { width: 30px; height: 30px; fill: var(--brand-blue); }

  .holder { position: absolute; left: 48px; top: 92px; color: var(--ink); }
  .holder-name { font-size: 23px; font-weight: 500; letter-spacing: 1px; }
  .holder-role { font-size: 10px; font-weight: 600; letter-spacing: 1px; margin-top: 3px; }

  .contact-text { position: absolute; font-size: 15px; line-height: 1.35; color: var(--ink); }
  .address { left: 320px; top: 105px; }
  .phones { left: 530px; top: 120px; }

  .web-text { position: absolute; left: 48px; top: 285px; color: var(--on-blue); font-size: 15px; line-height: 1.45; }

  .social-list { position: absolute; left: 400px; top: 218px; list-style: none; }
  .social-item { display: flex; align-items: center; height: 46px; color: var(--on-blue); font-size: 15px; }
  .social-dot { width: 32px; height: 32px; border-radius: 50%; background: var(--on-blue); margin-right: 12px; }
</style>
</head>
<body>

<section class="card card--front">
  <div class="brand">
    <span class="brand-mark"></span>
    <span class="brand-name">Cleanwarden</span>
  </div>
</section>

<section class="card card--back">
  <div class="info-band"></div>

  <div class="icon-badge" style="left:80px; top:40px;">
    <svg viewBox="0 0 24 24"><circle cx="12" cy="8" r="4.5"/><path d="M3.5 21c0-4.7 3.8-7.5 8.5-7.5s8.5 2.8 8.5 7.5z"/></svg>
  </div>
  <div class="holder">
    <div class="holder-name">TOM PELLWORTH</div>
    <div class="holder-role">SALES &amp; PRODUCT DEVELOPMENT</div>
  </div>

  <div class="icon-badge" style="left:370px; top:50px;">
    <svg viewBox="0 0 24 24"><path d="M12 2a7 7 0 0 0-7 7c0 5 7 13 7 13s7-8 7-13a7 7 0 0 0-7-7zm0 9.5A2.5 2.5 0 1 1 12 6.5a2.5 2.5 0 0 1 0 5z"/></svg>
  </div>
  <div class="contact-text address">174 Marlow St, Fernhollow<br>Brisbane 4108, Australia</div>

  <div class="icon-badge" style="left:585px; top:65px;">
    <svg viewBox="0 0 24 24"><path d="M8 2h8a2 2 0 0 1 2 2v16a2 2 0 0 1-2 2H8a2 2 0 0 1-2-2V4a2 2 0 0 1 2-2zm0 3v12h8V5zm4 13.5a1 1 0 1 0 0 2 1 1 0 0 0 0-2z"/></svg>
  </div>
  <div class="contact-text phones">Mob 0498 352 619<br>Tel 07 3941 2586</div>

  <div class="icon-badge icon-badge--light" style="left:90px; top:205px;">
    <svg viewBox="0 0 24 24"><path d="M2 4h20v13H2zm2 2v9h16V6zM9 19h6v2H9z"/></svg>
  </div>
  <div class="web-text">tom@cleanwarden.com.au<br>www.cleanwarden.com.au</div>

  <ul class="social-list">
    <li class="social-item"><span class="social-dot"></span>friendpage.com/cleanwarden</li>
    <li class="social-item"><span class="social-dot"></span>chirper.com/cleanwarden</li>
    <li class="social-item"><span class="social-dot"></span>workfolio.com/in/cleanwarden</li>
  </ul>
</section>

</body>
</html>
```